One pager Business Profile BrightHire

We would like to create a onepage with our company profile. It is important to keep the basis like it is in the word document but make it nice and fancy. Consistancy in color and fonts is important.

I've added the logo so you can pick the correct colors. The small logo's you can reuse, I want to replace them once you are ready.

In the word document we used standard Word stuff, I would like nice symbols and a professional well designed block in the Cooperation part

I would like to have a source file so I can change (and translate) text, so better to use a regular font or free font (I need the font than).

Target Market(s)

Recruitment

Industry/Entity Type

Recruitment

Requirements
Must have
• a professional look

```html
<!DOCTYPE html>
<html lang="en">
<head>
<meta charset="utf-8">
<title>BrightHire – Business Profile</title>
<link rel="stylesheet" href="https://fonts.googleapis.com/css2?family=Montserrat:wght@500&family=Oswald:wght@300;600&family=Playfair+Display:wght@900&family=Roboto+Condensed:wght@700&family=Roboto:wght@300;400;500;700&display=swap">
<style>
  :root {
    --navy: #16305e;
    --navy-deep: #152f5b;
    --blue: #0b72b9;
    --blue-dark: #0a64a6;
    --sky: #2ba3e3;
    --sky-pale: #9fcdef;
    --orange: #ef6a4c;
    --slate: #8e96a3;
    --ink: #1a1a1a;
    --grey-text: #444;
    --canvas: #ececec;
    --white: #ffffff;
  }
  * { box-sizing: border-box; margin: 0; padding: 0; }
  html, body { width: 1200px; height: 1200px; overflow: hidden; background: var(--canvas); }
  body { position: relative; font-family: 'Roboto', Arial, sans-serif; }

  .profile {
    position: absolute; left: 133px; top: 0;
    width: 1118px; height: 1438px;
    background: var(--white);
    transform: scale(0.8345); transform-origin: top left;
  }
  .shapes { position: absolute; inset: 0; width: 1118px; height: 1438px; }
  .abs { position: absolute; }

  .brand {
    left: 0; right: 0; top: 34px; text-align: center;
    font-family: 'Montserrat', sans-serif; font-weight: 500;
    font-size: 28px; letter-spacing: 6px; color: var(--navy);
  }
  .headline {
    left: 0; right: 0; top: 72px; text-align: center;
    font-family: 'Playfair Display', Georgia, serif; font-weight: 900;
    font-size: 61px; line-height: 72px; letter-spacing: -1px; color: var(--blue);
  }
  .headline .accent { color: var(--navy); }
  .subline {
    left: 0; right: 0; top: 136px; text-align: center;
    font-weight: 400; font-size: 31px; color: var(--grey-text);
  }
  .quote {
    left: 40px; right: 40px; top: 209px; text-align: center;
    font-family: 'Roboto Condensed', 'Arial Narrow', sans-serif; font-weight: 700;
    font-size: 31px; line-height: 38px; color: var(--white);
  }
  .copy { font-size: 17.5px; line-height: 21.3px; text-align: justify; text-align-last: left; }
  .copy p + p { margin-top: 10px; }
  .offer-network { left: 215px; top: 390px; width: 354px; color: var(--white); }
  .offer-main { left: 215px; top: 506px; width: 354px; color: var(--white); }
  .reviews { left: 653px; top: 341px; width: 400px; color: var(--ink); text-align: left; }
  .openness { left: 661px; top: 662px; width: 369px; color: var(--ink); }
  .openness p + p { margin-top: 11px; }

  .open-tag {
    left: 717px; top: 599px; width: 257px; height: 42px; border-radius: 21px;
    background: var(--blue); color: var(--white);
    font-weight: 500; font-size: 19px; line-height: 42px; text-align: center;
  }
  .group-note {
    left: 30px; right: 30px; top: 888px; text-align: center;
    font-size: 19px; line-height: 24px; color: var(--ink);
  }

  .teams-title {
    left: 128px; top: 1004px;
    font-family: 'Roboto Condensed', sans-serif; font-weight: 700;
    font-size: 29px; color: var(--sky);
  }
  .expertise-list { left: 128px; top: 1050px; list-style: none; color: var(--white); font-size: 18px; }
  .expertise-list li { position: relative; height: 32px; line-height: 24px; padding-left: 23px; }
  .expertise-list li::before {
    content: ""; position: absolute; left: 0; top: 5px; width: 13px; height: 13px;
    border: 1.5px solid var(--white); border-radius: 50%;
  }
  .expertise-list li::after {
    content: ""; position: absolute; left: 5px; top: 7px; width: 4px; height: 7px;
    border-right: 1.5px solid var(--white); border-bottom: 1.5px solid var(--white);
    transform: rotate(40deg);
  }

  .cooperation-diagram {
    left: 570px; top: 1012px; width: 490px; height: 310px; border-radius: 18px;
    background: linear-gradient(90deg, var(--slate) 0%, var(--sky-pale) 45%, var(--orange) 75%, var(--sky) 100%);
    opacity: 0.85;
  }

  .contact { top: 1374px; color: var(--navy); white-space: nowrap; }
  .contact-address { left: 78px; font-size: 18px; line-height: 28px; font-style: normal; }
  .contact-phone, .contact-mail { font-size: 21px; line-height: 28px; display: flex; align-items: center; gap: 6px; }
  .contact-phone { left: 588px; }
  .contact-mail { left: 820px; }
</style>
</head>
<body>
<main class="profile">
  <svg class="shapes" viewBox="0 0 1118 1438" xmlns="http://www.w3.org/2000/svg">
    <!-- quote band -->
    <rect x="0" y="190" width="1118" height="113" fill="var(--blue)"/>
    <rect x="283" y="303" width="553" height="4" fill="var(--navy)"/>

    <!-- offer block -->
    <polygon points="30,328 143,328 183,371 598,371 598,473 178,473 138,441 30,441" fill="var(--navy)"/>
    <polygon points="173,345 598,345 598,363 189,363" fill="var(--blue)"/>
    <polygon points="30,451 133,451 173,483 598,483 598,838 30,838" fill="var(--blue)"/>
    <rect x="128" y="483" width="72" height="355" fill="var(--blue-dark)" opacity="0.45"/>
    <text x="80" y="423" text-anchor="middle" font-family="Oswald, sans-serif" font-weight="300" font-size="88" fill="none" stroke="#fff" stroke-width="1.6">15</text>
    <rect x="55" y="505" width="48" height="285" rx="24" fill="#fff"/>
    <text transform="translate(89 647) rotate(-90)" text-anchor="middle" font-family="Montserrat, sans-serif" font-weight="500" font-size="29" letter-spacing="5" fill="var(--navy)">OUR OFFER</text>

    <!-- client badges -->
    <g role="img" aria-label="Cluster of client badges">
      <circle cx="676" cy="481" r="22" fill="#f6c500"/>
      <circle cx="731" cy="460" r="25" fill="#1b2f8f"/>
      <circle cx="791" cy="451" r="20" fill="#f39a1c"/>
      <circle cx="850" cy="450" r="27" fill="#17306b"/>
      <circle cx="906" cy="451" r="20" fill="#123c8c"/>
      <circle cx="963" cy="460" r="25" fill="#1f2a6e"/>
      <circle cx="1018" cy="483" r="24" fill="#138a4d"/>
      <circle cx="776" cy="489" r="18" fill="#49a9e0"/>
      <circle cx="817" cy="485" r="15" fill="#e0262e"/>
      <circle cx="883" cy="485" r="14" fill="#1e63b3"/>
      <circle cx="923" cy="489" r="17" fill="#d8232a"/>
      <circle cx="719" cy="515" r="25" fill="#dcdcdc"/>
      <circle cx="771" cy="526" r="18" fill="#c9202a"/>
      <circle cx="810" cy="515" r="13" fill="#111"/>
      <circle cx="850" cy="505" r="17" fill="#9aa0a8"/>
      <circle cx="891" cy="515" r="11" fill="#1d2f6a"/>
      <circle cx="930" cy="526" r="18" fill="#2f9a47"/>
      <circle cx="976" cy="515" r="25" fill="#f26a21"/>
      <circle cx="801" cy="541" r="10" fill="#b0b0b0"/>
      <rect x="821" y="528" width="60" height="30" rx="3" fill="#1c1c1c"/>
      <rect x="815" y="558" width="72" height="4" rx="2" fill="#8a8a8a"/>
      <circle cx="898" cy="541" r="9" fill="#e23b2e"/>
    </g>

    <!-- transparency box -->
    <path d="M710 619 H636 V838 H1055 V619 H982" fill="none" stroke="#222" stroke-width="2"/>

    <!-- divider -->
    <rect x="30" y="864" width="1058" height="1.5" fill="var(--navy)"/>
    <rect x="283" y="862" width="553" height="5" fill="var(--blue)"/>

    <!-- expertise panel -->
    <rect x="0" y="982" width="1118" height="368" fill="var(--navy-deep)"/>
    <rect x="76" y="983" width="29" height="79" fill="var(--sky)"/>
    <rect x="76" y="1270" width="29" height="80" fill="var(--sky)"/>
    <text transform="translate(102 1167) rotate(-90)" text-anchor="middle" font-family="Roboto Condensed, sans-serif" font-weight="700" font-size="32" fill="#fff">EXPERTISES</text>
    <line x1="531" y1="1008" x2="531" y2="1332" stroke="var(--sky)" stroke-width="2" stroke-dasharray="2 5"/>
  </svg>

  <div class="abs brand">BRIGHTHIRE</div>
  <h1 class="abs headline">BETTER EXPERTS, <span class="accent">FASTER</span></h1>
  <div class="abs subline">The best developers in our network</div>
  <blockquote class="abs quote">“ We offer our professionals only if we are convinced of their<br>competences and skills ”</blockquote>

  <div class="abs copy offer-network">
    <p>We have access to a specialist network of software development professionals carefully built up over a period of 15 years</p>
  </div>
  <div class="abs copy offer-main">
    <p>BrightHire helps you solve your IT organisation's capacity problems by offering and deploying high-quality, highly developed candidates.</p>
    <p>Our candidates, our professionals, are driven, and they are used to getting the best out of themselves and their project. They bring up-to-date knowledge for you, so they immediately tap the best level for you as a client to help achieve the objectives of the project, and therefore really complement your team. Our professionals are of immediate value and deliver demonstrable results..</p>
  </div>

  <div class="abs copy reviews">
    <p>By employing qualitatively suitable candidates,<br>we receive positive customer reviews and<br>score high customer satisfaction.</p>
  </div>

  <div class="abs open-tag">TRANSPARANT &amp; OPEN</div>
  <div class="abs copy openness">
    <p>BrightHire stands for transparency and openness, for both client and contractor.</p>
    <p>Clear agreements and no unnecessary obligations.</p>
    <p>Short lines, and smooth response times. For both the client and the professional.</p>
  </div>

  <p class="abs group-note">As part of the CoreValue Group and our partner network, BrightHire is able to provide clients with<br>full development teams, complete with test automators, scrum masters, product owners and business analysts<br>and developers..</p>

  <h2 class="abs teams-title">TEAMS</h2>
  <ul class="abs expertise-list">
    <li>Backend developers</li>
    <li>Frontend developers (component frameworks)</li>
    <li>Enterprise developers</li>
    <li>Data engineers</li>
    <li>Devops (Cloud platforms)</li>
    <li>Web developers</li>
    <li>Testers (automation &amp; functioneel)</li>
    <li>Mobile developers (native apps)</li>
    <li>UX/UI developers</li>
  </ul>

  <div class="abs cooperation-diagram" role="img" aria-label="Cooperation diagram: group, network partners and client joined through the company to freelance developers, with customer request arrows on both sides"></div>

  <address class="abs contact contact-address">BrightHire&nbsp; | &nbsp;Lindenlaan 24&nbsp; | &nbsp;3511 KP&nbsp; Utrecht</address>
  <div class="abs contact contact-phone">
    <svg width="20" height="20" viewBox="0 0 24 24"><path fill="var(--blue)" d="M6.6 10.8a15.1 15.1 0 0 0 6.6 6.6l2.2-2.2a1 1 0 0 1 1-.25 11.4 11.4 0 0 0 3.6.57 1 1 0 0 1 1 1V20a1 1 0 0 1-1 1A17 17 0 0 1 3 4a1 1 0 0 1 1-1h3.5a1 1 0 0 1 1 1c0 1.25.2 2.45.57 3.57a1 1 0 0 1-.25 1z"/></svg>
    <span>0031 30 555 01 84</span>
  </div>
  <div class="abs contact contact-mail">
    <svg width="19" height="19" viewBox="0 0 24 24" fill="none" stroke="var(--blue)" stroke-width="2"><circle cx="12" cy="12" r="9.5"/><ellipse cx="12" cy="12" rx="4" ry="9.5"/><line x1="2.5" y1="12" x2="21.5" y2="12"/></svg>
    <span>info@brighthire.nl</span>
  </div>
</main>
</body>
</html>
```